Website for New Medical Professional Organization Anti-Aging

Thanks to all who participated in my logo design project! We had several very good options to choose from, but we decided to go with the project attached by Remko.

Now, we need to develop the same idea into a web page. Our membership will be professionals involved in anti-aging medicine including doctors, naturopaths, chiropractors, nurses, nurse practioners, etc and also the corporations that have an interest eg. testing facilities, pharmacies, etc.

The sections will be :\
About Us
Membership
Certification
Conferences
Directory
Classifieds
Community

We need at least 2 areas for pictures that change content. One large one smaller.

1. Banner for the top, which includes the Logo, social media contacts, phone number, website address www.vlorbex.ca. We are thinking of using the black backround for the banner, then white backround with black and gold headings for the body.

2. Banner for footer: black again with small logo and contact information

3. The corporate sponsor banner can go across the bottom just above the footer banner. This one can be moving right to left to reveal the corporate sponsor names.

We need a section for "Join Now" where they are lead to a place to enter name, profession, address, email, phone, etc.

We need a nice looking "cart" for purchases on the webpage...

Our competition (and leader in the field is www.q7tz.com. We like some of their ideas, but it looks disorganized and too commercial. We want to look professional but friendly and interesting.
Updates

I am hoping that you all can "see" the logo on the black backround ... I can't see it on mine because I don't have editing software... I really like the gold logo on black as the designer provided.

Thanks and good luck!

I chose a gold colour from the colour wheel, but what I really want is for the logo colour to be present in the website design and become a prominent part of the design. Thanks for your work so far!

Marla

Hello designers!

I really like the ones that have more black in them. I would like to see more use of the Logo - make it bigger and a more integral pat of the website design. Since we are Canadian, we probably should have some red somewhere too :) So, now I am thinking Gold, Black, White and Red. I am not liking the silver I have seen so far. Please try to make the gold more regal and glowing. Thanks!

Marla

Target Market(s)

professionals - doctors, chiropractors, naturopaths, nurses
commercial health providers - pharmacy, testing facilities, etc

Industry/Entity Type

Nurse

Colors
ffcf3e
000000
d5d5d5

Requirements
Must have
• social media
contact info
e commerce

```html
<!DOCTYPE html>
<html lang="en">
<head>
<meta charset="utf-8">
<title>Canadian Guild of Longevity Medicine</title>
<link href="https://fonts.googleapis.com/css2?family=Open+Sans:wght@400;600;700&family=Arimo:wght@400;700&family=Great+Vibes&display=swap" rel="stylesheet">
<style>
:root{
  --black:#0b0b0b;
  --gold:#f3c332;
  --gold-light:#ffd95a;
  --gold-dark:#d9a81c;
  --gold-text:#c9a24a;
  --grey:#d5d5d5;
  --ink:#2b2b2b;
  --body:#444;
  --footer:#3b3b3b;
  --red:#c8281e;
  --white:#fff;
}
*{margin:0;padding:0;box-sizing:border-box}
html,body{width:783px;height:1200px;overflow:hidden;background:var(--white)}
body{position:relative;font-family:'Arimo',Arial,sans-serif;color:var(--body)}
.abs{position:absolute}
.header{left:0;top:0;width:783px;height:82px;background:linear-gradient(#2a2a2a,#050505)}
.brand{left:112px;top:22px;display:flex;align-items:center;gap:8px}
.brand-mark{width:36px;height:36px;border-radius:50%;background:var(--gold-text)}
.brand-name{font-family:'Open Sans',sans-serif;font-weight:600;color:var(--gold-text);font-size:12.5px;line-height:14px;letter-spacing:.5px;text-transform:uppercase}
.contact-bar{right:110px;top:38px;display:flex;align-items:center;gap:8px;color:var(--white);font-size:10px;font-family:'Open Sans',sans-serif}
.contact-bar svg{display:block}
.social-dot{width:16px;height:16px;border-radius:50%;background:#e6e6e6}
.nav{left:0;top:82px;width:783px;height:43px;background:linear-gradient(var(--gold-light),var(--gold) 60%,var(--gold-dark))}
.nav ul{list-style:none;display:flex;position:absolute;left:112px;top:0;height:43px}
.nav li{height:43px;display:flex;align-items:center;justify-content:center;white-space:nowrap;color:var(--white);font-family:'Open Sans',sans-serif;font-size:8.6px;border-right:1px solid rgba(160,110,0,.35)}
.nav li.active{background:#262626}
.hero{left:0;top:125px;width:783px;height:362px;background:linear-gradient(100deg,#cfe6f4 0%,#b7d8ee 45%,#e8c6a6 68%,#dcb08a 85%,#a6c9e2 100%)}
.hero-text{left:114px;top:203px;font-family:'Great Vibes',cursive;font-size:24px;line-height:30px;color:#2d2d2d;white-space:nowrap}
.slider{left:340px;top:458px;width:100px;height:16px;border:1px solid #8aa9c6;border-radius:3px;background:#f2f4f6;display:flex;align-items:center;gap:5px;padding-left:9px}
.slider .dot{width:5px;height:5px;border-radius:50%;background:#aaa}
.slider .dot.on{background:#333}
.welcome{left:0;top:487px;width:783px;height:116px;background:linear-gradient(#fff,#d9d9d9);text-align:center}
.welcome h1{font-family:'Open Sans',sans-serif;font-weight:400;font-size:17px;color:var(--ink);margin-top:16px}
.welcome p{font-size:8.3px;line-height:14.5px;color:#444;width:480px;margin:6px auto 0}
.btn{display:inline-block;background:linear-gradient(var(--gold-light),var(--gold-dark));color:var(--white);font-family:'Open Sans',sans-serif;font-weight:700;border-radius:2px}
.welcome .btn{width:78px;height:22px;line-height:22px;font-size:8.5px;margin-top:8px}
.section-title{font-family:'Open Sans',sans-serif;font-weight:600;font-size:12.2px;color:var(--ink);white-space:nowrap}
.sub-title{font-family:'Open Sans',sans-serif;font-weight:400;font-size:11px;color:var(--ink);white-space:nowrap}
.photo{background:linear-gradient(135deg,#8fc83a,#d8e9a4 55%,#e8c9a8)}
.about-text{left:300px;top:647px;width:168px;height:90px;overflow:hidden;font-size:7.8px;line-height:12.8px;text-align:justify;color:#555}
.about .btn{left:301px;top:742px;width:55px;height:15px;line-height:15px;font-size:7.5px;text-align:center;font-weight:400}
.video{left:486px;top:647px;width:183px;height:110px;background:linear-gradient(135deg,#e8eef4,#c9d7e6 50%,#e9c9a9)}
.play{left:562px;top:687px;width:30px;height:30px;border-radius:50%;background:rgba(40,40,40,.55)}
.blog{left:115px;top:804px;width:266px;height:102px;background:linear-gradient(#f6f7f8,#dcdfe3);border:1px solid #c3c6ca}
.blog-photo{left:11px;top:16px;width:71px;height:63px;background:linear-gradient(135deg,#cfd6de,#5c6470)}
.date{left:0;top:0;width:18px;height:16px;background:var(--gold);font-size:5.5px;font-weight:700;color:#222;line-height:7px;text-align:center;padding-top:1px}
.blog h3{position:absolute;left:90px;top:21px;font-size:7.8px;font-weight:400;color:#222;white-space:nowrap}
.blog p{position:absolute;left:91px;top:35px;width:166px;height:55px;overflow:hidden;font-size:7px;line-height:11px;color:#777;text-align:justify}
.card{top:804px;width:134px;height:102px;background:linear-gradient(#f6f7f8,#dcdfe3);border:1px solid #c3c6ca;text-align:center}
.avatar{width:40px;height:40px;border-radius:50%;background:linear-gradient(#d9c3ad,#9a7d62);border:2px solid #fff;margin:5px auto 0;box-shadow:0 0 0 1px #bbb}
.card .name{font-size:6.5px;color:#222;margin-top:4px}
.card .when{font-size:5.5px;color:#444}
.card .quote{font-size:6.2px;line-height:8.8px;color:#555;margin:4px 8px 0 12px;position:relative}
.q{position:absolute;color:var(--red);font-size:10px;line-height:10px}
.sponsors-head{left:111px;top:929px;display:flex;align-items:center;width:561px}
.sponsors-head .rule{flex:1;height:4px;border-top:1px solid #aaa;border-bottom:1px solid #aaa;margin-left:8px}
.sponsor{top:963px;height:18px;font-family:'Open Sans',sans-serif;font-weight:600;font-size:13px;display:flex;align-items:center;gap:5px;white-space:nowrap}
.sponsor .mk{width:12px;height:12px;border-radius:50%}
.footer{left:0;top:1022px;width:783px;height:110px;background:var(--footer)}
.footer .line{left:0;top:27px;width:783px;height:1px;background:#5a5a5a}
.col{top:14px;color:var(--white);font-size:8px;white-space:nowrap}
.col h4{font-size:7.8px;font-weight:400;text-transform:uppercase;margin-bottom:14px}
.col li{list-style:none;line-height:11.2px}
.col.contact{font-size:6.5px}
.bottom{left:0;top:1132px;width:783px;height:68px;background:#111}
.copy{left:114px;top:27px;font-size:6.8px;color:#ddd}
.socials{left:303px;top:18px;display:flex;gap:5px}
.socials span{width:22px;height:22px;border-radius:50%;background:#e8e8e8;border:2px solid #bbb}
.newsletter{left:536px;top:20px;width:135px;height:16px;background:var(--white);font-size:6.5px;color:#888;padding:4px 0 0 5px}
.newsletter svg{position:absolute;right:3px;top:2px}
</style>
</head>
<body>

<header class="header abs">
  <div class="brand abs">
    <div class="brand-mark"></div>
    <div class="brand-name">Canadian Guild<br>of Longevity Medicine</div>
  </div>
  <div class="contact-bar abs">
    <svg width="11" height="8" viewBox="0 0 11 8"><rect x=".5" y=".5" width="10" height="7" fill="none" stroke="#f3c332"/><path d="M.5 .5 5.5 4.5 10.5 .5" fill="none" stroke="#f3c332"/></svg>
    <span>info@vlorbex.ca</span>
    <svg width="12" height="12" viewBox="0 0 12 12" style="margin-left:6px"><circle cx="6" cy="6" r="5.3" fill="none" stroke="#f3c332"/><path d="M4 3.5c0 2.5 1.7 4.6 4.3 5l.7-1.2-1.4-.8-.6.7C6 6.6 5.4 6 5 5.1l.7-.6-.8-1.4z" fill="#f3c332"/></svg>
    <span>555.014.2290</span>
    <span class="social-dot" style="margin-left:6px" aria-label="Social link"></span>
    <span class="social-dot" aria-label="Social link"></span>
    <span class="social-dot" aria-label="Social link"></span>
  </div>
</header>

<nav class="nav abs">
  <ul>
    <li class="active" style="width:41px">HOME</li>
    <li style="width:58px">ABOUT US</li>
    <li style="width:69px">MEMBERSHIP</li>
    <li style="width:73px">CERTIFICATION</li>
    <li style="width:73px">CONFERENCES</li>
    <li style="width:61px">DIRECTORY</li>
    <li style="width:61px">CLASSIFIEDS</li>
    <li style="width:67px">COMMUNITY</li>
    <li style="width:57px;border-right:0">CONTACT US</li>
  </ul>
</nav>

<section class="hero abs" role="img" aria-label="Banner photo of a woman applying face cream with a red maple leaf against a blue sky"></section>
<p class="hero-text abs">We are a canadian medical professional<br>organisation working towards Anti Aging.</p>
<div class="slider abs">
  <svg width="12" height="8" viewBox="0 0 12 8"><path d="M3.5 1 1 4l2.5 3" fill="none" stroke="#222" stroke-width="1.5"/><path d="M8.5 1 11 4 8.5 7" fill="none" stroke="#999" stroke-width="1.5"/></svg>
  <span class="dot"></span><span class="dot"></span><span class="dot on"></span><span class="dot"></span><span class="dot"></span><span class="dot"></span>
</div>

<section class="welcome abs">
  <h1>WELCOME TO CGLM</h1>
  <p>Our membership will be professionals involved in anti-aging medicine including doctors, naturopaths, chiropractors, nurses, nurse practioners, etc and also the corporations that have an interest eg. testing facilities, pharmacies</p>
  <span class="btn">READ MORE</span>
</section>

<section class="about">
  <h2 class="section-title abs" style="left:110px;top:624px">CANADIAN MEDICAL PROFESSIONAL ORGANISATION</h2>
  <div class="photo abs" style="left:112px;top:647px;width:183px;height:110px" role="img" aria-label="Photo of a woman touching her cheek among green leaves"></div>
  <p class="about-text abs">Our membership will be professionals involved in anti-aging medicine including doctors, naturopaths, chiropractors, nurses, nurse practioners, etc and also the corporations that have an interest eg. testing facilities, pharmacies, Our membership will be professionals involved in anti-aging medicine including doctors,</p>
  <span class="btn abs">Read More</span>
  <h2 class="section-title abs" style="left:487px;top:624px">VIDEO</h2>
  <div class="video abs" role="img" aria-label="Video still of a patient receiving a facial treatment from gloved hands"></div>
  <div class="play abs"><svg width="30" height="30" viewBox="0 0 30 30"><path d="M12 9v12l10-6z" fill="#fff"/></svg></div>
</section>

<h2 class="sub-title abs" style="left:118px;top:784px">BLOG</h2>
<article class="blog abs">
  <div class="blog-photo abs" role="img" aria-label="Photo of a woman reading a tablet">
    <div class="date abs">13<br>MAY</div>
  </div>
  <h3>The complete guide for training your biceps</h3>
  <p>consectetur adipiscing elit. Nullam in dui mauris. Vivamus hendrerit arcu sed erat molestie vehicula. Sed auctor neque eu tellus rhoncus ut eleifend nibh porttitor. Ut in nulla enim. Phasellus molestie magna</p>
</article>

<h2 class="sub-title abs" style="left:394px;top:784px">LATEST TESTIMONIALS</h2>
<div class="card abs" style="left:392px">
  <div class="avatar" role="img" aria-label="Member portrait"></div>
  <div class="name">Clara Voss</div>
  <div class="when">on 22 Jan 2014</div>
  <div class="quote"><span class="q" style="left:-9px;top:-2px">“</span>There are many variations of passages of Lorem Ipsum available, but the majority<span class="q" style="right:-6px;bottom:-9px">”</span></div>
</div>
<div class="card abs" style="left:533px">
  <div class="avatar" role="img" aria-label="Member portrait"></div>
  <div class="name">Clara Voss</div>
  <div class="when">on 22 Jan 2014</div>
  <div class="quote"><span class="q" style="left:-9px;top:-2px">“</span>There are many variations of passages of Lorem Ipsum available, but the majority<span class="q" style="right:-6px;bottom:-9px">”</span></div>
</div>

<div class="sponsors-head abs"><h2 class="sub-title">OUR SPONSORS</h2><span class="rule"></span></div>
<div class="sponsor abs" style="left:124px;color:#1d3f7a"><span class="mk" style="background:#1d3f7a"></span>Veraluxe</div>
<div class="sponsor abs" style="left:250px;color:#2a66a8">Thyrobel</div>
<div class="sponsor abs" style="left:368px;color:#3b6fa8">ONDROVA</div>
<div class="sponsor abs" style="left:486px;color:#1c5ea8"><span class="mk" style="background:#1c5ea8"></span>PHARMETIS</div>
<div class="sponsor abs" style="left:590px;color:#2b3f70;font-size:10px">Calden Sciences</div>

<footer class="footer abs">
  <div class="line abs"></div>
  <div class="col abs" style="left:114px"><h4>Disclaimer</h4><ul><li>Personal Injury</li><li>Fall Accidents</li><li>Dog Bites</li><li>Accidents</li><li>Companies</li><li>Brain Injury</li></ul></div>
  <div class="col abs" style="left:201px"><h4>Sitemap</h4><ul><li>Personal Injury</li><li>Fall Accidents</li><li>Dog Bites</li><li>Compensation</li><li>Companies</li><li>Brain Injury</li></ul></div>
  <div class="col abs" style="left:288px"><h4>Privacy Policy</h4><ul><li>Personal Injury</li><li>Fall Accidents</li><li>Compensation</li><li>Accidents</li><li>Companies</li><li>Brain Injury</li></ul></div>
  <div class="col abs" style="left:393px"><h4>Reviews</h4><ul><li>Personal Injury</li><li>Fall Accidents</li><li>Dog Bites</li><li>Accidents</li><li>Companies</li><li>Brain Injury</li></ul></div>
  <div class="col abs" style="left:479px"><h4>Practice Areas</h4><ul><li>Personal Injury</li><li>Fall Accidents</li><li>Dog Bites</li><li>Compensation</li><li>Companies</li><li>Brain Injury</li></ul></div>
  <div class="col contact abs" style="left:577px"><h4>Contact Us</h4><ul><li>CGLM</li><li>P.O. Box 4827</li><li>Halden Bay, Nova Scotia</li><li>Phone: +1 555 014 7731</li><li>Email: info@vlorbex.ca</li></ul></div>
</footer>

<div class="bottom abs">
  <p class="copy abs">Copy Right © 2014. All rights reserved.</p>
  <div class="socials abs" aria-label="Social links"><span></span><span></span><span></span><span></span><span></span><span></span></div>
  <div class="newsletter abs">News Letter
    <svg width="18" height="12" viewBox="0 0 18 12"><rect x="1" y="1" width="16" height="10" fill="none" stroke="#333" stroke-width="1.5"/><path d="M1 1l8 6 8-6" fill="none" stroke="#333" stroke-width="1.5"/></svg>
  </div>
</div>

</body>
</html>
```